BUSINESS book cover

Publishing a book for a specific industry and hope to customize it for different industries in the future. So, design needs to be flexible. I want BRIGHT (possibly orange) cover with large words for title...really do not need illustration. Just the subtitle will change for future editions. Book is going to be 5.25" x 8"

Sorry for any confusion. The title of the book is: "Where Stories Bend Sideways..." The subtitle is: A Comprehensive Member Expderience Guide for Today's Club Management Professional

```html
<!DOCTYPE html>
<html lang="en">
<head>
<meta charset="utf-8">
<title>Where Stories Bend Sideways – Book Cover</title>
<link rel="stylesheet" href="https://fonts.googleapis.com/css2?family=Anton&family=Oswald:wght@500;700&family=PT+Sans:wght@400;700&family=PT+Sans+Narrow&display=swap">
<style>
  :root {
    --cover-orange: #f7890c;
    --deep-orange: #c96400;
    --ink: #2a2a2a;
    --title-white: #ffffff;
    --outline: #5a3a1a;
    --photo-dark: #3a3a3a;
    --photo-light: #bdbdbd;
  }
  html, body {
    margin: 0;
    padding: 0;
    width: 1200px;
    height: 852px;
    overflow: hidden;
    background: var(--cover-orange);
  }
  .cover {
    position: relative;
    width: 1200px;
    height: 852px;
    background: var(--cover-orange);
    overflow: hidden;
  }
  .cover-art {
    position: absolute;
    inset: 0;
  }
  .display-title {
    font-family: "Anton", "Oswald", sans-serif;
  }
  .back-tagline {
    position: absolute;
    left: 76px;
    top: 98px;
    width: 441px;
    margin: 0;
    text-align: center;
    font-family: "PT Sans", sans-serif;
    font-size: 19px;
    line-height: 21px;
    font-weight: 700;
    color: var(--ink);
  }
  .back-blurb {
    position: absolute;
    left: 76px;
    top: 154px;
    width: 441px;
    font-family: "PT Sans", sans-serif;
    font-size: 13.8px;
    line-height: 18px;
    font-weight: 700;
    color: var(--ink);
    text-align: justify;
  }
  .back-blurb p { margin: 0 0 18px; }
  .author-photo {
    position: absolute;
    left: 76px;
    top: 524px;
    width: 234px;
    height: 156px;
    background: linear-gradient(135deg, var(--photo-dark), var(--photo-light) 55%, #ececec);
  }
  .author-bio {
    position: absolute;
    left: 324px;
    top: 522px;
    width: 193px;
    height: 176px;
    overflow: hidden;
    margin: 0;
    font-family: "PT Sans Narrow", sans-serif;
    font-size: 13.2px;
    line-height: 17.2px;
    color: var(--ink);
    text-align: justify;
  }
</style>
</head>
<body>
<main class="cover">
  <svg class="cover-art" width="1200" height="852" viewBox="0 0 1200 852" aria-label="Where Stories Bend Sideways book cover">
    <!-- back cover edge title -->
    <text class="display-title back-edge-title" transform="translate(2,6) rotate(90)" font-size="54" fill="var(--deep-orange)">WHERE STORIES BEND SIDEWAYS</text>

    <!-- spine -->
    <text class="display-title spine-title" transform="translate(579,82) rotate(90)" font-size="56" textLength="520" lengthAdjust="spacingAndGlyphs" fill="var(--title-white)" stroke="var(--outline)" stroke-width="1.2" paint-order="stroke">WHERE STORIES BEND SIDEWAYS</text>
    <text class="spine-author" transform="translate(580,653) rotate(90)" font-family="Oswald, sans-serif" font-weight="700" font-size="50" textLength="142" lengthAdjust="spacingAndGlyphs" fill="var(--ink)">DALE MARSH</text>

    <!-- front cover title -->
    <g class="front-title display-title" fill="var(--title-white)" stroke="var(--outline)" stroke-width="1.4" paint-order="stroke">
      <text x="670" y="133" font-size="96" textLength="493" lengthAdjust="spacingAndGlyphs">WHERE STORIES</text>
      <text x="670" y="331" font-size="208" textLength="493" lengthAdjust="spacingAndGlyphs">BEND</text>
      <text x="742" y="393" font-size="54" textLength="350" lengthAdjust="spacingAndGlyphs">SIDE</text>
      <text x="670" y="680" font-size="325" textLength="493" lengthAdjust="spacingAndGlyphs">WAYS</text>
    </g>

    <!-- subtitle -->
    <g class="front-subtitle" font-family="Oswald, sans-serif" font-weight="500" font-size="28" fill="var(--ink)">
      <text x="672" y="725" textLength="482" lengthAdjust="spacingAndGlyphs">A COMPREHENSIVE MEMBER EXPERIENCE GUIDE</text>
      <text x="670" y="757" textLength="488" lengthAdjust="spacingAndGlyphs">FOR TODAY'S CLUB MANAGEMENT PROFESSIONAL</text>
    </g>

    <!-- front author -->
    <text class="front-author" x="908" y="822" text-anchor="middle" font-family="Oswald, sans-serif" font-weight="700" font-size="52" textLength="252" lengthAdjust="spacingAndGlyphs" fill="var(--ink)">DALE MARSH</text>
  </svg>

  <h2 class="back-tagline">The <em>most</em> important work of art is <em>the</em> life <em>that</em> we create.</h2>

  <div class="back-blurb">
    <p>In The Maker's Heart, Adrian Lowell Pierce—author, thought leader, and founder of HARBOR in Portland—pens a manifesto for human creativity and the beginning of a new renais-sance. Pierce not only calls us to reclaim our creative essence but reveals how we can craft our lives into a work of art. There are no shortcuts to quality, and Pierce celebrates the spiritual process that can help us discover our true selves.</p>
    <p>Pierce demonstrates that we all carry within us the essence of an artist. We all need to create, to be a part of a process that brings to the world something beautiful, good, and true, in order to allow our souls to come to life. It's not only the quality of the ingredients we use to build our lives that matters, but the care we bring to the process itself. Just as with baking artisan bread, it's a process that's crafted over time. And God is the master artisan of our lives. With poignant, inspirational stories and insights from art, life, history, and scripture interspersed throughout, Pierce walks readers through the process of crafting a life of beauty and wonder.</p>
  </div>

  <div class="author-photo" role="img" aria-label="Black and white portrait photograph of the author"></div>

  <p class="author-bio">Pierce demonstrates that we all carry within us the essence of an artist. We all need to create, to be a part of a process that brings to the world something beautiful, good, and true, in order to allow our souls to come to life. It's not only the quality of the ingredients we use to build our lives that matters, but the care we bring to the p</p>
</main>
</body>
</html>
```